Calloway Pipeworks Summary ESG brochure report

We are looking to create a summary ESG report for and Oil and Gas Midstream producer - Calloway Pipeworks. This is a report on their environmental, social and governance (ESG) aspects as well as a summary of who they are. It's focused on Wyoming oil and gas midstream for pipeline transport of oil and gas. We are to emphasize their environmental aspects, social aspects with visuals, graphics, etc. Attached is a example ESG report that is larger than what we want, but gives the designer of what an ESG report is.
The attached Harrowgate 2019 report is an "IDEA of what we are looking for - but on a smaller scale. This is a much larger report, but expands on the idea of what we are trying to do.
Client is:
https://www.callowaypipeworks.example/
The outline brochure documens is what we have written and given examples of graphics with our writing / bullets of what we have visioned through the brochure. We are looking for a document with these items and graphs in it.
We have attached a few excel sheets and creations to hopefully better visualize our ideas and timelines to assist the graphic designers.
Look and feel
Each slider illustrates characteristics of the customer's brand and the style your logo design should communicate.

```html
<!DOCTYPE html>
<html lang="en">
<head>
<meta charset="utf-8">
<title>Calloway Pipeworks – The Path to Value in the Rockies</title>
<link rel="stylesheet" href="https://fonts.googleapis.com/css2?family=Open+Sans:wght@600;700&display=swap">
<style>
  :root {
    --backdrop: #b4b3b9;
    --paper: #ececec;
    --earth: #673b19;
    --meadow: #79a72c;
    --photo-tone: #4a80c2;
    --ink: #2b2b2b;
    --headline: #f4f4f4;
  }
  * { margin: 0; padding: 0; box-sizing: border-box; }
  html, body {
    width: 1200px; height: 814px; overflow: hidden;
    background: var(--backdrop);
    font-family: "Open Sans", Arial, sans-serif;
  }
  .canvas {
    width: 1200px; height: 814px;
    display: flex; align-items: center; justify-content: center;
  }
  .cover {
    position: relative;
    width: 540px; height: 740px;
    background: var(--paper);
    overflow: hidden;
  }
  .brand {
    position: absolute; top: 52px; right: 48px;
    display: flex; align-items: center; gap: 12px;
    color: var(--ink); font-weight: 600;
  }
  .brand-dot {
    width: 30px; height: 30px; border-radius: 50%;
    background: var(--earth);
  }
  .brand-name {
    font-size: 17px; line-height: 1.05; letter-spacing: 0.08em;
    text-transform: uppercase;
  }
  .earth-column {
    position: absolute; left: 150px; top: 160px;
    width: 120px; height: 580px;
    background: var(--earth);
  }
  .earth-base {
    position: absolute; left: 0; bottom: 0;
    width: 445px; height: 160px;
    background: var(--earth);
  }
  .meadow-block {
    position: absolute; left: 0; top: 190px;
    width: 235px; height: 390px;
    background: var(--meadow);
  }
  .landscape {
    position: absolute; left: 235px; top: 178px;
    width: 230px; height: 460px;
    background: var(--photo-tone);
  }
  .headline {
    position: absolute; left: 252px; top: 205px; width: 206px;
    color: var(--headline); font-weight: 600;
    text-transform: uppercase; line-height: 0.98;
  }
  .headline .lead { display: block; font-size: 24px; letter-spacing: 0.01em; }
  .headline .place { display: block; font-size: 45px; font-weight: 700; margin-top: 2px; }
</style>
</head>
<body>
  <main class="canvas">
    <article class="cover">
      <div class="brand">
        <span class="brand-dot"></span>
        <span class="brand-name">Calloway<br>Pipeworks</span>
      </div>
      <div class="earth-column"></div>
      <div class="earth-base"></div>
      <div class="meadow-block" role="img" aria-label="Green panel with fine topographic contour texture"></div>
      <div class="landscape" role="img" aria-label="Photograph of a Rocky Mountain valley under a blue sky"></div>
      <h1 class="headline">
        <span class="lead">The path to<br>value in the</span>
        <span class="place">Rockies</span>
      </h1>
    </article>
  </main>
</body>
</html>
```